Flat bootstrap design for existing site

I'm looking for a modern flat design based around an existing logo. This has to be a custom design (no external templates), and implemented into a bootstrap framework.

The logo is attached as 2 versions - choose whichever you want, that flows better with whatever design you choose.

Added screenshots of the existing site (currently using the default bootstrap layouts). Please make your designs around those pages in the screenshots (i.e. the homepage only has the postal code input and the header). The active page has 3 screenshots, because I wanted to illustrate the other states that would be visible (in the table rows).

This is a moving/junk removal website, just for some context.

Here's some example websites (flat designs) that I like, just to give you an idea of what I'm after.

https://www.plivento.com/
https://hoskadel.com/
https://trumvex.com/
https://bravolinth.com/en/

• It must be a modern/simple flat design, that is built around the existing logo (attached).
• It has to be implemented using bootstrap.

```html
<!DOCTYPE html>
<html lang="en">
<head>
<meta charset="utf-8">
<title>Haulvo – Become a Driver</title>
<link href="https://fonts.googleapis.com/css2?family=Roboto:wght@300;400;500;700&display=swap" rel="stylesheet">
<style>
  :root {
    --brand: #45c7f4;
    --brand-dark: #0a6a8f;
    --brand-mid: #0790c6;
    --ink: #5a5a5a;
    --ink-soft: #7b7b7b;
    --field-border: #cfcfcf;
    --white: #ffffff;
    --page-top: #ffffff;
    --page-bottom: #e7e8ec;
  }
  * { box-sizing: border-box; margin: 0; padding: 0; }
  html, body { width: 1200px; height: 855px; overflow: hidden; }
  body {
    font-family: "Roboto", sans-serif;
    background: linear-gradient(180deg, var(--page-top) 0%, var(--page-top) 30%, var(--page-bottom) 100%);
    position: relative;
    color: var(--ink);
  }
  .site-header {
    position: absolute; left: 0; top: 0; width: 1200px; height: 97px;
    background: var(--white); border-bottom: 1px solid #ececec;
  }
  .site-header::before {
    content: ""; position: absolute; left: 98px; right: 98px; top: 0; height: 1px; background: #e2e2e2;
  }
  .brand {
    position: absolute; left: 99px; top: 30px;
    display: flex; align-items: center; gap: 10px;
    font-weight: 700; font-size: 36px; color: var(--brand); letter-spacing: 1px;
  }
  .brand-dot { width: 22px; height: 22px; border-radius: 50%; background: var(--brand); }
  .main-nav { position: absolute; left: 480px; top: 34px; display: flex; align-items: center; }
  .main-nav a {
    text-decoration: none; color: var(--ink-soft); font-size: 17px; text-transform: uppercase;
    margin-right: 16px; display: flex; align-items: center; gap: 8px;
  }
  .main-nav a.is-active {
    background: var(--brand); color: var(--white); padding: 10px 15px; border-radius: 20px;
  }
  .social { position: absolute; left: 1008px; top: 34px; display: flex; gap: 12px; }
  .social span { width: 40px; height: 40px; border-radius: 50%; border: 2px solid var(--brand); display: block; }

  .hero-title {
    position: absolute; left: 96px; top: 135px;
    font-size: 62px; font-weight: 700; color: var(--brand); letter-spacing: -0.3px;
  }
  .hero-lead {
    position: absolute; left: 97px; top: 207px;
    font-size: 27px; font-weight: 300; color: var(--ink);
  }

  .apply-form { position: absolute; left: 98px; top: 280px; width: 488px; }
  .field {
    position: absolute; left: 0; width: 488px; height: 41px;
    background: var(--white); border: 1px solid var(--field-border); border-radius: 4px;
    display: flex; align-items: center; justify-content: space-between; padding: 0 12px 0 22px;
    font-size: 14px; font-weight: 300; color: var(--ink);
  }
  .field.select { background: linear-gradient(180deg, #ffffff, #ececec); }
  .field svg { width: 26px; height: 26px; stroke: var(--brand); fill: none; stroke-width: 1.3; }
  .btn-apply {
    position: absolute; left: 0; top: 456px; width: 488px; height: 60px; border: none; border-radius: 4px;
    background: linear-gradient(180deg, var(--brand-mid), var(--brand-dark));
    color: var(--white); font-family: "Roboto", sans-serif; font-weight: 700; font-size: 17px;
  }

  .radius-card {
    position: absolute; left: 613px; top: 280px; width: 488px; height: 172px;
    background: var(--brand); border-radius: 4px; padding: 21px 24px;
  }
  .radius-card h2 { color: var(--white); font-size: 26px; font-weight: 500; line-height: 32px; }
  .km-input {
    margin-top: 18px; margin-left: -3px; width: 176px; height: 41px; border: 1px solid var(--white);
    border-radius: 21px; display: flex; align-items: center; justify-content: space-between;
    padding: 0 14px 0 18px; color: var(--white); font-size: 16px; font-weight: 300;
  }
  .km-input svg { width: 22px; height: 22px; stroke: var(--white); fill: none; stroke-width: 1.3; }

  .truck-scene {
    position: absolute; left: 604px; top: 488px; width: 570px; height: 348px;
    background: linear-gradient(180deg, #c9cacd 0%, #e3e4e7 60%, #f4f4f5 100%);
    border-bottom: 2px solid #222;
  }
</style>
</head>
<body>
  <header class="site-header">
    <div class="brand"><span class="brand-dot"></span>HAULVO</div>
    <nav class="main-nav">
      <a href="#">Book</a>
      <a href="#">How it works</a>
      <a href="#" class="is-active">Become a driver</a>
      <a href="#">Sign in
        <svg width="14" height="14" viewBox="0 0 14 14" fill="none" stroke="#45c7f4" stroke-width="1.3"><path d="M1 7h8M6 4l3 3-3 3M11 1v12"/></svg>
      </a>
    </nav>
    <div class="social"><span></span><span></span></div>
  </header>

  <h1 class="hero-title">Interested in becoming a driver?</h1>
  <p class="hero-lead">Complete this form, and we’ll assess it and get back to you.</p>

  <form class="apply-form">
    <div class="field" style="top:0">First Name
      <svg viewBox="0 0 26 26"><circle cx="13" cy="13" r="12"/><path d="M8 22c0-4 2-6 5-6s5 2 5 6M13 15c-3 0-4-3-4-5s1-4 4-4 4 2 4 4-1 5-4 5z"/></svg></div>
    <div class="field" style="top:47px">Last Name
      <svg viewBox="0 0 26 26"><circle cx="13" cy="13" r="12"/><path d="M8 22c0-4 2-6 5-6s5 2 5 6M13 15c-3 0-4-3-4-5s1-4 4-4 4 2 4 4-1 5-4 5z"/></svg></div>
    <div class="field" style="top:92px">E-mail
      <svg viewBox="0 0 26 26"><rect x="1" y="5" width="24" height="16"/><path d="M1 5l12 10 12-10M1 21l9-8M25 21l-9-8"/></svg></div>
    <div class="field" style="top:136px">Password
      <svg viewBox="0 0 26 26"><rect x="4" y="12" width="18" height="12"/><path d="M8 12V8a5 5 0 0 1 10 0"/><circle cx="13" cy="18" r="1.5"/></svg></div>

    <div class="field" style="top:215px">Phone
      <svg viewBox="0 0 26 26"><path d="M6 3l4 5-2 3c1 3 4 6 7 7l3-2 5 4-3 3C12 23 3 14 3 6z"/><path d="M15 5a6 6 0 0 1 6 6M15 1a10 10 0 0 1 10 10"/></svg></div>
    <div class="field" style="top:262px">Address
      <svg viewBox="0 0 26 26"><path d="M13 20s7-7 7-12a7 7 0 0 0-14 0c0 5 7 12 7 12z"/><circle cx="13" cy="8" r="2.5"/><path d="M5 18l-3 7h22l-3-7"/></svg></div>
    <div class="field" style="top:307px">City
      <svg viewBox="0 0 26 26"><rect x="4" y="8" width="8" height="17"/><rect x="12" y="2" width="10" height="23"/><path d="M15 6h4M15 10h4M15 14h4M15 18h4M7 12h2M7 16h2M7 20h2"/></svg></div>
    <div class="field select" style="top:352px">Province
      <svg viewBox="0 0 26 26" style="width:12px;height:12px"><path d="M6 10h14l-7 7z" fill="#777" stroke="none"/></svg></div>
    <div class="field" style="top:396px">Postal Code
      <svg viewBox="0 0 26 26"><path d="M2 11v14h22V11L13 3z"/><rect x="6" y="6" width="14" height="10"/><path d="M2 25l9-7h4l9 7M9 9h8M9 12h8"/></svg></div>

    <button type="button" class="btn-apply">APPLY</button>
  </form>

  <section class="radius-card">
    <h2>How Many km away from your home do you want to service?</h2>
    <div class="km-input">Kilometers
      <svg viewBox="0 0 22 22"><circle cx="11" cy="11" r="9"/><path d="M11 11l4-4M5 11h1M16 11h1M11 5v1"/></svg></div>
  </section>

  <div class="truck-scene" role="img" aria-label="Illustration of a recycling garbage truck with a worker in front of grey city buildings, next to two recycling bins"></div>
</body>
</html>
```